GRAY HARBOR PLAN

Our business will reach out to business owners and offer a variety of services, predominantly the following: a) a free review of the owner's business structure to make sure it was properly formed, b) litigation representation at an extremely discounted rate (we plan to engage in direct marketing to civil litigation defendants, c) weekly "attorney letters" at no charge, d) free legal forms that are commonly used in business, and e) by far, the most important service offered is the licensed use of a copyrighted clause that is incorporated into virtually any commercial agreement (hereafter referred to as "the Clause").
The effect of the Clause is to require that parties to a contract ("Contract") notify each other, in writing, of any fact or event (referred to as "Event") that might impact the Contract. And the failure to comply with the Clause results in the non-complying party being given a significant advantage should the Contract become the subject of a lawsuit, in particular, an advantage over issues commonly referred to "he said / she said" issues. We believe that most civil litigation hinges on at least one or more of such issues, i.e., issues for which there is no concrete proof one way or the other. In such cases, the party taking advantage of the Clause will very likely prevail on all such issues -- in other words, using the Clause will likely prevent litigation from being pursued against such party, or likely result in such party prevailing in court. ARE ALL THESE SERVICES WORTH $9.95 PER WEEK?

Target Market(s)

#1. Current defendants in civil litigation cases, #2 business owners who get sued by: a) employees, b) business associates, who believe they have claims against the owner or the business.

Industry/Entity Type

Legal claims are increasing in large part because of the leverage that exists in forcing businesses to hire legal counsel to defend "he said / she said" claims -

Number of Pages Required

1 page

Colors
0094D4
00A9DD
6FCCEA
C7EBF8
E9F6FB

Requirements
Must have
• Professional appearance. We are explaining that there are wolves out there in the form of employees and business associates who can turn into enemies by making groundless allegations that could easily cost tens of thousands of dollars -- and it does more frequently than you might think.
Nice to have
• I like to refer to Tom Wexley's classic axiom: an ounce of prevention is worth a pound of cure -- with anecdotes taken from actual examples of why the services offered, i.e., the extreme discount of legal fees in the event of a lawsuit, being able to send attorney letters sent out every week at no charge, and above all, the right to incorporate copyrighted contractual provisions that make it very difficult for employees and business associates to make claims against you that evolve into lawsuits -- are each worth far more than the paltry membership fee of $9.95 per week.

```html
<!DOCTYPE html>
<html lang="en">
<head>
<meta charset="utf-8">
<title>Gray Harbor Plan</title>
<link rel="stylesheet" href="https://fonts.googleapis.com/css2?family=IBM+Plex+Sans:wght@500;600;700&family=Roboto:wght@400;500;700&display=swap">
<style>
:root{
  --teal:#087b85;
  --teal-dark:#066a73;
  --ink:#1a1a1a;
  --text:#6b6b6b;
  --dark:#141414;
  --band:#f4f4f4;
  --white:#ffffff;
}
*{box-sizing:border-box;margin:0;padding:0}
html,body{width:1200px;height:3698px;overflow:hidden}
body{position:relative;font-family:'Roboto',sans-serif;color:var(--ink);background:var(--white)}
.abs{position:absolute}
.heading{font-family:'IBM Plex Sans',sans-serif;font-weight:700}

/* hero */
.hero{position:absolute;left:0;top:0;width:1200px;height:650px;background:linear-gradient(90deg,#121212 0%,#1a1a1a 35%,#5d4e3f 60%,#8a7868 80%,#a99c8d 100%)}
.hero-photo{position:absolute;left:470px;top:110px;width:730px;height:540px;background:radial-gradient(ellipse at 50% 45%,rgba(210,200,190,.35),rgba(60,50,40,0) 70%)}
.brand{left:110px;top:38px;color:var(--white);font-family:'IBM Plex Sans',sans-serif;font-weight:600;font-size:23px;letter-spacing:.5px}
.nav{left:463px;top:40px;display:flex;gap:23px}
.nav a{color:var(--white);text-decoration:none;font-size:15px;font-weight:500}
.call{left:906px;top:28px;display:flex;align-items:center;gap:12px;color:var(--white)}
.call-icon{width:36px;height:36px;border-radius:50%;background:var(--teal);display:flex;align-items:center;justify-content:center}
.call small{display:block;font-size:12px}
.call strong{display:block;font-size:19px;font-weight:500;margin-top:2px}
.hero-title{left:110px;top:270px;color:var(--white);font-size:38px;letter-spacing:.5px}
.hero-text{left:110px;top:333px;width:440px;color:var(--white);font-size:16px;font-weight:500;line-height:28px}
.btn{display:inline-flex;align-items:center;gap:9px;background:var(--teal);color:var(--white);border-radius:30px;font-weight:500;font-size:16px;text-decoration:none;justify-content:center}
.hero-btn{left:112px;top:413px;width:204px;height:49px}

/* welcome */
.portrait{left:115px;top:735px;width:430px;height:502px;border-radius:50%;background:radial-gradient(ellipse at 50% 40%,#dcdcdc,#8a8a8a 70%,#3a3a3a)}
.eyebrow{left:636px;top:766px;color:var(--teal);font-family:'IBM Plex Sans',sans-serif;font-weight:600;font-size:19px;display:flex;align-items:center;gap:12px}
.eyebrow span{display:inline-block;width:80px;height:3px;background:var(--teal)}
.welcome-title{left:636px;top:795px;font-size:39px;color:var(--ink)}
.welcome-text{left:636px;top:868px;width:452px;font-size:14px;line-height:26.6px;color:var(--text);text-align:justify}
.welcome-btn{left:636px;top:1166px;width:179px;height:43px;font-size:15px}

/* services */
.services{position:absolute;left:0;top:1322px;width:1200px;height:1386px;background:var(--band)}
.section-title{position:absolute;left:0;width:1200px;text-align:center;font-size:39px;color:var(--ink)}
.section-title em{font-style:normal;color:var(--teal)}
.section-title::after{content:"";display:block;width:70px;height:3px;background:var(--teal);margin:6px auto 0}
.services-intro{left:210px;top:140px;width:780px;text-align:center;font-size:15px;line-height:27px;color:#444}
.services-intro b{color:var(--teal);font-weight:500}
.service-photo{position:absolute;width:474px;height:300px}
.card{position:absolute;width:436px;height:230px;background:var(--white);border-top:4px solid var(--teal);box-shadow:0 4px 14px rgba(0,0,0,.08);text-align:center;overflow:hidden}
.card h3{font-size:17.5px;font-weight:500;line-height:27px;margin:24px 36px 0;text-transform:uppercase;color:var(--ink)}
.card p{font-size:13.5px;line-height:24px;color:var(--text);margin:12px 34px 0}
.card .more{position:absolute;right:0;bottom:0;width:150px;height:40px;background:var(--teal);color:var(--white);font-size:15px;font-weight:500;display:flex;align-items:center;justify-content:center;padding-left:14px;clip-path:polygon(14% 0,100% 0,100% 100%,0 100%)}
.card.active{background:var(--teal);border-top-color:var(--white)}
.card.active h3,.card.active p{color:var(--white)}
.card.active .more{background:var(--white);color:var(--teal)}

/* faq */
.faq-item{position:absolute;left:221px;width:758px;height:55px;border-radius:28px;background:var(--white);box-shadow:0 2px 10px rgba(0,0,0,.12);display:flex;align-items:center;justify-content:space-between;padding:0 22px 0 24px;font-size:15px;font-weight:500;color:#333}
.faq-item.open{height:128px;border-radius:30px;background:var(--teal);color:var(--white);display:block;padding:24px 24px}
.faq-item.open .q{display:flex;justify-content:space-between;align-items:center}
.faq-item.open p{font-weight:400;font-size:13.5px;line-height:23px;margin-top:12px;padding-left:4px}

/* footer */
.footer{position:absolute;left:0;top:3377px;width:1200px;height:321px;background:var(--dark);color:var(--white);text-align:center}
.footer-brand{position:absolute;left:0;top:55px;width:1200px;font-family:'IBM Plex Sans',sans-serif;font-weight:600;font-size:33px}
.footer-contact{position:absolute;left:0;top:120px;width:1200px;font-size:15px;display:flex;justify-content:center;gap:26px;align-items:center}
.footer-contact span{display:inline-flex;align-items:center;gap:8px}
.footer-nav{position:absolute;left:0;top:154px;width:1200px;font-size:14px;font-weight:700;display:flex;justify-content:center;gap:24px}
.copyright{position:absolute;left:0;top:194px;width:1200px;font-size:13px}
.copyright u{margin:0 4px}
.socials{position:absolute;left:500px;top:242px;display:flex;gap:9px}
.socials span{width:43px;height:43px;border-radius:50%;background:#d9d9d9}
.socials span:first-child{background:var(--teal)}
</style>
</head>
<body>

<header class="hero">
  <div class="hero-photo" role="img" aria-label="Photo of smiling business colleagues reviewing documents at a laptop"></div>
  <div class="abs brand">GRAYHARBORPLAN.NET</div>
  <nav class="abs nav"><a href="#">Home</a><a href="#">About Us</a><a href="#">Our Services</a><a href="#">FAQ</a><a href="#">Contact Us</a></nav>
  <div class="abs call">
    <div class="call-icon"><svg width="18" height="18" viewBox="0 0 24 24"><path fill="#fff" d="M6.6 10.8a15.1 15.1 0 0 0 6.6 6.6l2.2-2.2c.3-.3.7-.4 1-.2 1.1.4 2.3.6 3.6.6.6 0 1 .4 1 1V20c0 .6-.4 1-1 1A17 17 0 0 1 3 4c0-.6.4-1 1-1h3.5c.6 0 1 .4 1 1 0 1.3.2 2.5.6 3.6.1.3 0 .7-.2 1z"/></svg></div>
    <div><small>Call or text us</small><strong>(555) 014-2290</strong></div>
  </div>
  <h1 class="abs hero-title heading">GRAY HARBOR PLAN</h1>
  <p class="abs hero-text">GRAY HARBOR PLAN (“GHP”) is a referral service that helps the business owner avoid LEGAL CONFLICT</p>
  <a class="abs btn hero-btn" href="#">GET STARTED
    <svg width="15" height="15" viewBox="0 0 16 16"><circle cx="8" cy="8" r="8" fill="#fff"/><path d="M6.5 4.5 10 8l-3.5 3.5" stroke="#087b85" stroke-width="2" fill="none"/></svg></a>
</header>

<section>
  <div class="abs portrait" role="img" aria-label="Engraved oval portrait of Tom Wexley"></div>
  <div class="eyebrow abs">WELCOME TO <span></span></div>
  <h2 class="abs welcome-title heading">GRAY HARBOR PLAN</h2>
  <p class="abs welcome-text">GRAY HARBOR PLAN (“GHP”) is a referral service that helps the business owner avoid LEGAL CONFLICT by referring attorneys who offer services uniquely designed to minimize – if not altogether eliminate – those conflicts that can and do evolve into COSTLY LITIGATION. And by “costly,” we mean that, in today's world, the costs of civil litigation have skyrocketed out of control, to the point that, in far too many cases, civil litigation is simply not affordable, giving those with superior economic means a disproportionately UNFAIR ADVANTAGE in the dispute resolution process. A membership in GHP levels the playing field.</p>
  <a class="abs btn welcome-btn" href="#">LEARN MORE
    <svg width="14" height="14" viewBox="0 0 16 16"><circle cx="8" cy="8" r="8" fill="#fff"/><path d="M6.5 4.5 10 8l-3.5 3.5" stroke="#087b85" stroke-width="2" fill="none"/></svg></a>
</section>

<section class="services">
  <h2 class="section-title heading" style="top:56px"><em>OUR</em> SERVICES</h2>
  <p class="abs services-intro">The price for membership is a ridiculously low <b>$9.95 PER WEEK.</b> We believe that this fee is very affordable. So what is it? Membership includes the following:</p>

  <div class="service-photo" style="left:112px;top:238px;background:linear-gradient(135deg,#e6e6e6,#5a6172 60%,#2d3142)" role="img" aria-label="Photo of lawyers reviewing a document at a table"></div>
  <div class="card" style="left:131px;top:497px">
    <h3>Civil Litigation Defense @<br>Discounted Rates</h3>
    <p>If you have been sued, you may have no choice but to hire an attorney or lawfirm to represent you, if you are, for example, a legal entity like a corporation</p>
    <div class="more">LEARN MORE</div>
  </div>

  <div class="service-photo" style="left:612px;top:238px;background:linear-gradient(135deg,#8a8f98,#b98a5c 50%,#3c3f47)" role="img" aria-label="Photo of smiling colleagues discussing a contract"></div>
  <div class="card active" style="left:631px;top:497px">
    <h3>Notification of Possible Breach<br>RE: Contracts</h3>
    <p>Very likely, the most important feature of our membership is the right torequire that parties to your contractual relationships notify you of events</p>
    <div class="more">LEARN MORE</div>
  </div>

  <div class="service-photo" style="left:112px;top:778px;background:linear-gradient(135deg,#4a3428,#8a7866 50%,#d8d2c8)" role="img" aria-label="Photo of a business meeting around a wooden table"></div>
  <div class="card" style="left:131px;top:1037px">
    <h3 style="margin-top:38px">Free Attorney Letters</h3>
    <p>Picture going to your mailbox and retrieving your mail. Then imagine going through each letter, sorting the “junk mail” from the rest.</p>
    <div class="more">LEARN MORE</div>
  </div>

  <div class="service-photo" style="left:612px;top:778px;background:linear-gradient(135deg,#dde2e6,#7d848c 55%,#c9c3b8)" role="img" aria-label="Photo of two colleagues reviewing papers in an office"></div>
  <div class="card" style="left:631px;top:1037px">
    <h3>Free Consultation / Review RE:<br>Business Formation</h3>
    <p>Often, businesses are formed without taking the ideal amount of time tothoroughly explore all of the ins and outs of business formation.</p>
    <div class="more">LEARN MORE</div>
  </div>
</section>

<section>
  <h2 class="section-title heading" style="top:2776px;font-size:34px"><em>FREQUENTLY</em> ASKED QUESTIONS</h2>
  <div class="faq-item" style="top:2871px">Lorem ipsum dolor sit amet, consectetur adipiscing elit, sed do <svg width="20" height="20" viewBox="0 0 16 16"><circle cx="8" cy="8" r="8" fill="#087b85"/><path d="M6.5 4.5 10 8l-3.5 3.5" stroke="#fff" stroke-width="2" fill="none"/></svg></div>
  <div class="faq-item" style="top:2942px">Sed ut perspiciatis unde omnis iste natus error <svg width="20" height="20" viewBox="0 0 16 16"><circle cx="8" cy="8" r="8" fill="#087b85"/><path d="M6.5 4.5 10 8l-3.5 3.5" stroke="#fff" stroke-width="2" fill="none"/></svg></div>
  <div class="faq-item" style="top:3012px">Nemo enim ipsam voluptatem quia voluptas sit aspernatur aut odit aut fugit <svg width="20" height="20" viewBox="0 0 16 16"><circle cx="8" cy="8" r="8" fill="#087b85"/><path d="M6.5 4.5 10 8l-3.5 3.5" stroke="#fff" stroke-width="2" fill="none"/></svg></div>
  <div class="faq-item" style="top:3084px">Neque porro quisquam est, qui dolorem ipsum quia <svg width="20" height="20" viewBox="0 0 16 16"><circle cx="8" cy="8" r="8" fill="#087b85"/><path d="M6.5 4.5 10 8l-3.5 3.5" stroke="#fff" stroke-width="2" fill="none"/></svg></div>
  <div class="faq-item open" style="top:3155px">
    <div class="q">Duis aute irure dolor in reprehenderit in voluptate velit esse cillum dolore eu fugiat <svg width="20" height="20" viewBox="0 0 16 16"><circle cx="8" cy="8" r="8" fill="#fff"/><path d="M4.5 6.5 8 10l3.5-3.5" stroke="#087b85" stroke-width="2" fill="none"/></svg></div>
    <p>At vero eos et accusamus et iusto odio dignissimos ducimus qui blanditiis praesentium<br>voluptatum deleniti atque corrupti quos dolores et quas</p>
  </div>
</section>

<footer class="footer">
  <div class="footer-brand">GRAYHARBORPLAN.NET</div>
  <div class="footer-contact">
    <span><svg width="14" height="14" viewBox="0 0 24 24"><path fill="#fff" d="M6.6 10.8a15.1 15.1 0 0 0 6.6 6.6l2.2-2.2c.3-.3.7-.4 1-.2 1.1.4 2.3.6 3.6.6.6 0 1 .4 1 1V20c0 .6-.4 1-1 1A17 17 0 0 1 3 4c0-.6.4-1 1-1h3.5c.6 0 1 .4 1 1 0 1.3.2 2.5.6 3.6.1.3 0 .7-.2 1z"/></svg>(555) 014-2290</span>
    <span>|</span>
    <span><svg width="12" height="16" viewBox="0 0 12 16"><path fill="#fff" d="M6 0a6 6 0 0 0-6 6c0 4.5 6 10 6 10s6-5.5 6-10a6 6 0 0 0-6-6zm0 8.5A2.5 2.5 0 1 1 6 3.5a2.5 2.5 0 0 1 0 5z"/></svg>2417 Tidewater Avenue, Marlow Bay, Oregon 97031, United States</span>
  </div>
  <nav class="footer-nav"><span>HOME</span><span>/</span><span>ABOUT US</span><span>/</span><span>OUR SERVICES</span><span>/</span><span>FAQ</span><span>/</span><span>CONTACT</span></nav>
  <div class="copyright">Copyright© 2022 <u>GRAYHARBORPLAN.NET</u> | All Rights Reserved</div>
  <div class="socials"><span></span><span></span><span></span><span></span></div>
</footer>

</body>
</html>
```